iron deficiency anemia - educational reference paper

looking for an educational paper/poster 8x11 or no larger than 11x14 that lists the most common foods with pictures and limited words a super rough outline attached - I wrote the words of the pictures (but would like to have the actual pictures of these items) I would like in roughly the same order
for the pictures for fatigue, headache....can be drawings or cartoons
double sided or single sided (which ever fits) see attached for categories (3 of them)

Target Market(s)

educational for people with limited education - thus not much wording

Requirements
Must have
• pictures, simple design

```html
<!DOCTYPE html>
<html lang="en">
<head>
<meta charset="utf-8">
<title>Iron Deficiency Anemia – Common Foods in Your Community</title>
<link rel="stylesheet" href="https://fonts.googleapis.com/css2?family=Montserrat:wght@300;500;800;900&display=swap">
<style>
  :root{
    --red:#d7141f;
    --orange:#f05a14;
    --navy:#0b3a8c;
    --ink:#1b1b1b;
    --frame:#8fd3f3;
    --sky-top:#ffffff;
    --sky-bottom:#c2e5f8;
    --card:#ffffff;
  }
  *{box-sizing:border-box;margin:0;padding:0}
  html,body{width:945px;height:1200px;overflow:hidden;background:#ffffff}
  body{font-family:"Montserrat",sans-serif;color:var(--ink)}
  .poster{
    position:relative;width:945px;height:1200px;overflow:hidden;
    background:linear-gradient(180deg,var(--sky-top) 0%,var(--sky-top) 18%,var(--sky-bottom) 100%);
  }
  .title{
    position:absolute;top:40px;left:0;width:100%;text-align:center;
    font-size:54px;line-height:1;letter-spacing:0.3px;white-space:nowrap;
  }
  .title .light{font-weight:300;color:var(--red)}
  .title .bold{font-weight:900;color:var(--orange)}
  .subtitle{
    position:absolute;top:102px;left:0;width:100%;
    display:flex;justify-content:center;align-items:center;gap:10px;
    font-weight:800;font-size:27px;line-height:32px;color:var(--navy);white-space:nowrap;
  }
  .subtitle .square{width:8px;height:8px;background:var(--red);display:inline-block}

  .section{
    position:absolute;left:48px;width:853px;
    background:var(--card);border:2px solid var(--frame);border-radius:16px;
  }
  .section-title{
    position:absolute;top:-17px;left:50%;transform:translateX(-50%);
    background:var(--orange);color:#fff;font-weight:900;font-size:30px;
    padding:0 22px;height:34px;line-height:35px;border-radius:15px;white-space:nowrap;
  }
  .meat{top:171px;height:233px}
  .beans{top:453px;height:220px}
  .seeds{top:726px;height:146px}
  .veg{top:923px;height:231px}

  .item{
    position:absolute;width:170px;
    left:calc(var(--x) * 1px - 85px);top:calc(var(--y) * 1px);
    text-align:center;
  }
  .art{
    position:absolute;left:50%;bottom:calc(100% + 6px);
    width:calc(var(--w) * 1px);height:calc(var(--h) * 1px);
    transform:translateX(-50%);
    border-radius:48% 52% 46% 54% / 52% 46% 54% 48%;
    background:radial-gradient(ellipse at 38% 34%, var(--c2) 0%, var(--c) 68%);
  }
  .label{display:block;font-weight:500;font-size:14px;line-height:16px;letter-spacing:0.2px;white-space:nowrap}
  .divider{position:absolute;left:330px;top:17px;width:1px;height:88px;background:#555}
</style>
</head>
<body>
<main class="poster">
  <h1 class="title"><span class="light">IRON DEFICIENCY </span><span class="bold">ANEMIA</span></h1>
  <p class="subtitle"><span class="square"></span>COMMON FOODS IN YOUR COMMUNITY<span class="square"></span></p>

  <section class="section meat">
    <h2 class="section-title">MEAT &amp; SEA FOOD</h2>
    <div class="item" style="--x:92;--y:104"><div class="art" style="--w:92;--h:70;--c:#a7844f;--c2:#d3b27c" role="img" aria-label="Sheep illustration"></div><span class="label">SHEEP/LAMB</span></div>
    <div class="item" style="--x:239;--y:104"><div class="art" style="--w:118;--h:60;--c:#c98f7c;--c2:#ecbcaa" role="img" aria-label="Pig illustration"></div><span class="label">PIG/PORK</span></div>
    <div class="item" style="--x:376;--y:104"><div class="art" style="--w:60;--h:70;--c:#d9551f;--c2:#f39a4e" role="img" aria-label="Chicken illustration"></div><span class="label">CHICKEN</span></div>
    <div class="item" style="--x:519;--y:104"><div class="art" style="--w:84;--h:66;--c:#6b4a2c;--c2:#3c8a4c" role="img" aria-label="Duck illustration"></div><span class="label">GOOSE DUCK</span></div>
    <div class="item" style="--x:668;--y:104"><div class="art" style="--w:86;--h:74;--c:#2e2e2e;--c2:#7a5a44" role="img" aria-label="Turkey illustration"></div><span class="label">TURKEY</span></div>
    <div class="item" style="--x:781;--y:104"><div class="art" style="--w:76;--h:70;--c:#7f8896;--c2:#c6ccd6" role="img" aria-label="Pigeon illustration"></div><span class="label">SQUAB</span></div>

    <div class="item" style="--x:97;--y:206"><div class="art" style="--w:76;--h:70;--c:#f3f3f3;--c2:#f7b518" role="img" aria-label="Fried egg illustration"></div><span class="label">EGG</span></div>
    <div class="item" style="--x:240;--y:206"><div class="art" style="--w:78;--h:56;--c:#6c8a48;--c2:#a3b878" role="img" aria-label="Clams illustration"></div><span class="label">CLAMS</span></div>
    <div class="item" style="--x:373;--y:206"><div class="art" style="--w:98;--h:66;--c:#f0842a;--c2:#fbd15a" role="img" aria-label="Shrimp illustration"></div><span class="label">SHRIMP</span></div>
    <div class="item" style="--x:544;--y:203"><div class="art" style="--w:148;--h:56;--c:#3a65a0;--c2:#6c96c9" role="img" aria-label="Whale illustration"></div><span class="label">WHALE</span></div>
    <div class="item" style="--x:721;--y:206"><div class="art" style="--w:98;--h:44;--c:#e0893c;--c2:#f6c27a" role="img" aria-label="Fish illustration"></div><span class="label">CUTTLEFISH HALIBUT</span></div>
  </section>

  <section class="section beans">
    <h2 class="section-title">BEANS &amp; PEAS</h2>
    <div class="item" style="--x:84;--y:83"><div class="art" style="--w:86;--h:64;--c:#6e1414;--c2:#a8352c" role="img" aria-label="Kidney beans illustration"></div><span class="label">KIDNEY BEAN</span></div>
    <div class="item" style="--x:218;--y:83"><div class="art" style="--w:80;--h:52;--c:#d7ae78;--c2:#f4e2c4" role="img" aria-label="Cow peas illustration"></div><span class="label">COW PEA</span></div>
    <div class="item" style="--x:372;--y:83"><div class="art" style="--w:72;--h:52;--c:#221d35;--c2:#4a4268" role="img" aria-label="Black beans illustration"></div><span class="label">BLACK BEAN</span></div>
    <div class="item" style="--x:505;--y:83"><div class="art" style="--w:60;--h:44;--c:#e2501c;--c2:#f48a4a" role="img" aria-label="Lentils illustration"></div><span class="label">LENTIL</span></div>
    <div class="item" style="--x:635;--y:83"><div class="art" style="--w:82;--h:58;--c:#6d8a28;--c2:#a3bb52" role="img" aria-label="Mung beans illustration"></div><span class="label">MUNG BEAN</span></div>
    <div class="item" style="--x:769;--y:83"><div class="art" style="--w:86;--h:62;--c:#e2bb6a;--c2:#f6e0a8" role="img" aria-label="Yellow beans illustration"></div><span class="label">YELLOW BEAN</span></div>

    <div class="item" style="--x:95;--y:185"><div class="art" style="--w:92;--h:58;--c:#c99f86;--c2:#ecd6c6" role="img" aria-label="Cranberry beans illustration"></div><span class="label">CRANBERRY BEAN</span></div>
    <div class="item" style="--x:248;--y:185"><div class="art" style="--w:110;--h:58;--c:#1f8a2e;--c2:#54c24a" role="img" aria-label="Pigeon peas in pod illustration"></div><span class="label">PIGEON PEA</span></div>
    <div class="item" style="--x:374;--y:185"><div class="art" style="--w:66;--h:58;--c:#eaaa2c;--c2:#f7d56e" role="img" aria-label="Chickpeas illustration"></div><span class="label">CHICKPEAS</span></div>
    <div class="item" style="--x:509;--y:183"><div class="art" style="--w:114;--h:62;--c:#5a9a36;--c2:#e8b64a" role="img" aria-label="Rice stalk illustration"></div><span class="label">RICE BRAN</span></div>
    <div class="item" style="--x:645;--y:183"><div class="art" style="--w:76;--h:58;--c:#9a1424;--c2:#cf3a46" role="img" aria-label="Adzuki beans illustration"></div><span class="label">ADUZKI BEAN</span></div>
    <div class="item" style="--x:773;--y:183"><div class="art" style="--w:94;--h:44;--c:#5fb022;--c2:#a6e04e" role="img" aria-label="Lima beans illustration"></div><span class="label">LIMA BEAN</span></div>
  </section>

  <section class="section seeds">
    <h2 class="section-title">SEEDS &amp; NUTS</h2>
    <div class="item" style="--x:99;--y:110"><div class="art" style="--w:94;--h:68;--c:#262626;--c2:#8a8a8a" role="img" aria-label="Sunflower seeds illustration"></div><span class="label">SUNFLOWER SEED</span></div>
    <div class="item" style="--x:257;--y:110"><div class="art" style="--w:100;--h:72;--c:#e4bb58;--c2:#f6e2a2" role="img" aria-label="Sesame seeds illustration"></div><span class="label">SESAME SEED</span></div>
    <div class="divider"></div>
    <div class="item" style="--x:409;--y:110"><div class="art" style="--w:108;--h:64;--c:#c9bea2;--c2:#efe9da" role="img" aria-label="Pumpkin seeds illustration"></div><span class="label">PUMPKIN SEED</span></div>
    <div class="item" style="--x:558;--y:110"><div class="art" style="--w:64;--h:66;--c:#e2c08a;--c2:#f6e6c8" role="img" aria-label="Cashew nut illustration"></div><span class="label">CASHUE NUT</span></div>
    <div class="item" style="--x:675;--y:110"><div class="art" style="--w:76;--h:70;--c:#a85a2c;--c2:#f0dcb4" role="img" aria-label="Almonds illustration"></div><span class="label">ALMONDS</span></div>
    <div class="item" style="--x:785;--y:110"><div class="art" style="--w:72;--h:66;--c:#6e7a24;--c2:#a8343c" role="img" aria-label="Pistachios illustration"></div><span class="label">PISTACHIO</span></div>
  </section>

  <section class="section veg">
    <h2 class="section-title">VEGETABLES</h2>
    <div class="item" style="--x:82;--y:102"><div class="art" style="--w:56;--h:70;--c:#3f7a2a;--c2:#7ab44e" role="img" aria-label="Spinach leaf illustration"></div><span class="label">SPINACH</span></div>
    <div class="item" style="--x:208;--y:102"><div class="art" style="--w:64;--h:66;--c:#5a0b24;--c2:#9a1c44" role="img" aria-label="Beet illustration"></div><span class="label">BEET</span></div>
    <div class="item" style="--x:344;--y:102"><div class="art" style="--w:110;--h:54;--c:#7fae4a;--c2:#cfe6a0" role="img" aria-label="Brussels sprouts illustration"></div><span class="label">BRUSSLE</span></div>
    <div class="item" style="--x:475;--y:102"><div class="art" style="--w:94;--h:74;--c:#2e6e24;--c2:#f0f0f0" role="img" aria-label="Turnip with greens illustration"></div><span class="label">TURNIP</span></div>
    <div class="item" style="--x:620;--y:102"><div class="art" style="--w:80;--h:64;--c:#3f9430;--c2:#a6d876" role="img" aria-label="Collard greens illustration"></div><span class="label">COLLARD GREENS</span></div>
    <div class="item" style="--x:767;--y:102"><div class="art" style="--w:70;--h:64;--c:#2a7a22;--c2:#8cc43e" role="img" aria-label="Broccoli illustration"></div><span class="label">BROCCOLI</span></div>

    <div class="item" style="--x:97;--y:202"><div class="art" style="--w:98;--h:66;--c:#5ca03a;--c2:#f4efd8" role="img" aria-label="Cauliflower illustration"></div><span class="label">CALIFLOWER</span></div>
    <div class="item" style="--x:225;--y:202"><div class="art" style="--w:74;--h:56;--c:#d01c1a;--c2:#f4623e" role="img" aria-label="Tomatoes illustration"></div><span class="label">TOMATO</span></div>
    <div class="item" style="--x:336;--y:202"><div class="art" style="--w:102;--h:50;--c:#ec6a1c;--c2:#7cc24a" role="img" aria-label="Carrot illustration"></div><span class="label">CARROT</span></div>
    <div class="item" style="--x:480;--y:202"><div class="art" style="--w:72;--h:50;--c:#9c7434;--c2:#d4ac62" role="img" aria-label="Potato illustration"></div><span class="label">POTATO</span></div>
    <div class="item" style="--x:633;--y:202"><div class="art" style="--w:68;--h:66;--c:#ea6a1c;--c2:#fbe0a0" role="img" aria-label="Mushroom illustration"></div><span class="label">MUSHROOMS</span></div>
    <div class="item" style="--x:767;--y:202"><div class="art" style="--w:54;--h:60;--c:#4a2270;--c2:#8a52b6" role="img" aria-label="Blackberries illustration"></div><span class="label">BLACKBERRY</span></div>
  </section>
</main>
</body>
</html>
```